Medical Company in need of Modern business card design for new Wound Care clinic.

Modern business card design for our Woundcare company. Logo and description of services can be found on our website; https://www.tovrel-woundcare.com/

```html
<!DOCTYPE html>
<html lang="en">
<head>
<meta charset="utf-8">
<title>Tovrel Woundcare – Business Card</title>
<link rel="stylesheet" href="https://fonts.googleapis.com/css2?family=Arimo:wght@400;700&family=Poppins:wght@400&family=Raleway:wght@500&display=swap">
<style>
  :root {
    --backdrop: #2d2d2d;
    --card: #000000;
    --gold: #c9923a;
    --gold-light: #ffcf72;
    --gold-dark: #b07f2c;
    --ink: #ffffff;
  }
  * { margin: 0; padding: 0; box-sizing: border-box; }
  html, body {
    width: 1200px; height: 1015px; overflow: hidden;
    background: var(--backdrop);
  }
  .sheet {
    width: 1200px; height: 1015px;
    display: flex; flex-direction: column; align-items: center; justify-content: center;
    gap: 56px;
  }
  .card {
    position: relative;
    width: 660px; height: 377px;
    background: var(--card);
    box-shadow: 0 14px 30px rgba(0,0,0,.55);
    overflow: hidden;
  }
  .gold-band {
    position: absolute; left: 0; right: 0; bottom: 34px; height: 9px;
    background: linear-gradient(180deg, var(--gold-light), var(--gold-dark));
  }

  /* Front */
  .card-front { text-align: center; }
  .brand {
    position: absolute; left: 0; right: 0; top: 92px;
    display: flex; align-items: center; justify-content: center; gap: 16px;
  }
  .brand-mark {
    width: 22px; height: 22px; background: var(--gold);
  }
  .brand-name {
    font-family: "Raleway", sans-serif; font-weight: 500;
    font-size: 30px; letter-spacing: 11px;
    color: var(--gold);
  }
  .services {
    position: absolute; left: 0; right: 0; top: 158px;
    list-style: none;
    font-family: "Poppins", sans-serif; font-weight: 400;
    font-size: 15px; line-height: 27px; color: var(--ink);
  }
  .services .divider { color: var(--gold); padding: 0 4px; }

  /* Back */
  .contact {
    position: absolute; left: 54px; top: 70px;
    font-family: "Arimo", sans-serif; color: var(--ink);
  }
  .person-name {
    font-weight: 700; font-size: 22px; color: var(--gold); letter-spacing: .5px;
  }
  .person-role { font-size: 15px; margin-top: 2px; letter-spacing: .3px; }
  .rule { width: 145px; height: 1px; background: var(--gold); margin: 22px 0 14px; }
  .contact-list { list-style: none; font-size: 17px; line-height: 26px; }
  .contact-list li { display: flex; align-items: center; gap: 10px; }
  .contact-list svg { width: 16px; height: 16px; flex: none; }
  .address { font-size: 17px; line-height: 24px; }
  .brand-large {
    position: absolute; right: 44px; top: 96px;
    display: flex; align-items: center; gap: 14px;
  }
  .brand-large .brand-mark { width: 30px; height: 30px; }
  .brand-large .brand-name { font-size: 44px; letter-spacing: 8px; }
</style>
</head>
<body>
<main class="sheet">
  <section class="card card-front">
    <div class="brand">
      <span class="brand-mark"></span>
      <span class="brand-name">TOVREL WOUNDCARE</span>
    </div>
    <ul class="services">
      <li>Hyperbaric Oxygen Therapy (HBO)<span class="divider">|</span>Debridement</li>
      <li>Advanced Wound Dressings</li>
      <li>Bio-engineered Skin Substitutes</li>
      <li>Compression Therapy and Edema Management</li>
    </ul>
    <div class="gold-band"></div>
  </section>

  <section class="card card-back">
    <div class="contact">
      <div class="person-name">MARCUS HALE</div>
      <div class="person-role">MANAGING DIRECTOR</div>
      <div class="rule"></div>
      <ul class="contact-list">
        <li>
          <svg viewBox="0 0 16 16" aria-hidden="true"><path d="M4 1.5l2.3 3-1.4 1.6c.8 1.9 2.5 3.6 4.4 4.4l1.6-1.4 3 2.3-1.4 2.6C7 13.7 2.3 9 1.5 3z" fill="var(--gold)"/></svg>
          044-987 654 321
        </li>
        <li>
          <svg viewBox="0 0 16 16" aria-hidden="true"><rect x="1" y="3.5" width="14" height="9" fill="none" stroke="var(--gold)" stroke-width="1.6"/><path d="M1 3.5l7 5 7-5" fill="none" stroke="var(--gold)" stroke-width="1.6"/></svg>
          info@tovrel-woundcare.com
        </li>
        <li>
          <svg viewBox="0 0 16 16" aria-hidden="true"><g fill="none" stroke="var(--gold)" stroke-width="1.3"><circle cx="8" cy="8" r="6.5"/><ellipse cx="8" cy="8" rx="3" ry="6.5"/><path d="M1.5 8h13M2.5 4.8h11M2.5 11.2h11"/></g></svg>
          www.tovrel-woundcare.com
        </li>
      </ul>
      <div class="rule"></div>
      <p class="address">218, Linden Park Avenue<br>60418, Northbrook</p>
    </div>
    <div class="brand-large">
      <span class="brand-mark"></span>
      <span class="brand-name">TOVREL</span>
    </div>
    <div class="gold-band"></div>
  </section>
</main>
</body>
</html>
```